Comfort Support Network Western Ridge Booklet and Resource cover design for use on various inhouse

We need a design using the attached art and logo which can be used in all inhouse brochure and booklet production so that we can assume a common image and look across all of our productions
Updates

Thanks for your designs.  I have posted them for voting with my staff and Board sub committee.  Is it possible to see some landscape versions.

Target Market(s)

People newly diagnosed with a terminal illness, health professionals caring for people with a terminal illness. family of people affected by terminal illness. Age 18-100, Male and female.

Industry/Entity Type

Council

Requirements
Must have
• The comfort support network of WR Logo
• The integration of the Aboriginal artwork into the design

```html
<!DOCTYPE html>
<html lang="en">
<head>
<meta charset="utf-8">
<title>Terminal Illness — Comfort Support Network WR</title>
<link rel="stylesheet" href="https://fonts.googleapis.com/css2?family=Josefin+Sans:wght@400;700&display=swap">
<style>
  :root {
    --artwork-earth: #7b5d2c;
    --artwork-red: #7a2a2c;
    --band-mauve: #cdbdc1;
    --title-plum: #3e2234;
    --subtitle-gold: #a8874c;
    --logo-card: #ffffff;
    --logo-ink: #3a3a3a;
    --logo-accent: #1bb0cf;
  }
  * { margin: 0; padding: 0; box-sizing: border-box; }
  html, body { width: 1200px; height: 800px; overflow: hidden; background: #fff; }
  .cover {
    position: relative;
    width: 1200px;
    height: 800px;
    overflow: hidden;
    font-family: "Josefin Sans", sans-serif;
  }
  .artwork {
    position: absolute;
    left: 0;
    width: 1200px;
    background: radial-gradient(circle at 30% 40%, var(--artwork-red) 0, transparent 60%),
                linear-gradient(135deg, var(--artwork-earth), #6a4e24);
  }
  .artwork--top { top: 0; height: 47px; }
  .artwork--bottom { top: 567px; height: 233px; }
  .title-band {
    position: absolute;
    top: 47px;
    left: 0;
    width: 1200px;
    height: 520px;
    background: var(--band-mauve);
    text-align: center;
  }
  .title {
    color: var(--title-plum);
    font-weight: 700;
    line-height: 1;
  }
  .title__line {
    display: block;
    font-size: 148px;
  }
  .title__line--first { margin-top: 80px; letter-spacing: 0.13em; padding-left: 0.13em; }
  .title__line--second { margin-top: 18px; letter-spacing: 0.29em; padding-left: 0.29em; }
  .subtitle {
    margin-top: 52px;
    color: var(--subtitle-gold);
    font-weight: 400;
    font-size: 38px;
    line-height: 66px;
    letter-spacing: 0.04em;
  }
  .logo-card {
    position: absolute;
    left: 383px;
    top: 630px;
    width: 434px;
    height: 115px;
    background: var(--logo-card);
    display: flex;
    align-items: center;
    justify-content: center;
    gap: 18px;
  }
  .logo-card__mark {
    width: 46px;
    height: 46px;
    border-radius: 50%;
    background: var(--logo-accent);
    flex: none;
  }
  .logo-card__name {
    color: var(--logo-ink);
    font-weight: 400;
    font-size: 30px;
    line-height: 1.1;
  }
</style>
</head>
<body>
  <main class="cover">
    <div class="artwork artwork--top" role="img" aria-label="Aboriginal dot painting artwork with red flower motifs on ochre ground"></div>
    <section class="title-band">
      <h1 class="title">
        <span class="title__line title__line--first">TERMINAL</span>
        <span class="title__line title__line--second">ILLNESS</span>
      </h1>
      <p class="subtitle">Health Professionals Caring<br>For People With A Terminal Illness</p>
    </section>
    <div class="artwork artwork--bottom" role="img" aria-label="Aboriginal dot painting artwork with red flower motifs on ochre ground"></div>
    <div class="logo-card">
      <span class="logo-card__mark"></span>
      <span class="logo-card__name">Comfort Support<br>Network WR</span>
    </div>
  </main>
</body>
</html>
```